Modern labels for Tidlock products

We need a new design of our labels for the product “Tidlock” (https://www.tidlock.eu/#) . The reason why we want to change our labels is to get a modern and more advanced look of our product. We also want to create a unique product that is attractive for our customers, even if the product are used in hospitals and healthcare centers for collecting dangerous waste.

There is three sizes of labels (55x95, 90x95, 170x95 mm) for different boxes, but the label will contain similar information. There are certain requirements and factors from regulations/standards that you need to follow when you create the new layout. But it’s up to you to change the design. You can work with background, fonts, effects, colors, structure, pattern, new symbols, logotype etc. The label could be any color, but the container will stay yellow so they have to look good together.

Keywords: Elegant, modern, functional, attractive, exclusive

Target Market(s)

Hospitals and healthcare centers

Industry/Entity Type

Product

Font styles to use
Serif
Sans Serif

Colors

Designer to choose colors to be used in the design.

Requirements
Must have
• Requirements for the regulations ADR UN3291 and ISO 23907 (PDF).
• * Symbol for danger waste
• * Filling level
• * "Danger"
• * Symbol for no second use
• * Symbol for manufaturer
• * Referencenumber
• * Text "”Clinical waste, Unspecified, N.O.S.”"
• * Area for series, certification, size and useful capacity
• * Area for Illustrations.
• * Text “Autoclavable at 134 c”, “Do not force closure” and “Do not overfill”.
• * Text for certification ”UN 3291 1H2/Y0,3/S/YR/N/KVP4817B”
• Three different sizes (55x95, 90x95, 170x95).
• More info in PDF "3kravspecifikation"
Nice to have
• A modern, elegant, advanced look of our label.
Should not have
• The information must be clear and readable, not too decorative/handwriting fonts.

```html
<!DOCTYPE html>
<html lang="en">
<head>
<meta charset="utf-8">
<title>Tidlock Clinical Waste Label</title>
<link href="https://fonts.googleapis.com/css2?family=Open+Sans:wght@400;600;700;800&display=swap" rel="stylesheet">
<style>
  :root {
    --black: #000000;
    --yellow: #f2eb1f;
    --navy: #2a2b62;
    --white: #ffffff;
    --grey: #2b2b2b;
  }
  * { box-sizing: border-box; margin: 0; padding: 0; }
  html, body { width: 1200px; height: 1138px; overflow: hidden; background: var(--white); }
  body { font-family: "Open Sans", Arial, sans-serif; }
  .label { position: relative; width: 1200px; height: 1138px; background: var(--black); overflow: hidden; }
  .abs { position: absolute; }

  .fill-level { top: 0; left: 0; width: 1200px; height: 94px; }
  .fill-level-text { top: 12px; left: 0; width: 1200px; text-align: center; color: var(--white); font-weight: 800; font-size: 48px; letter-spacing: 1px; line-height: 70px; }
  .chevrons { top: 34px; height: 26px; }
  .chevrons.left { left: 12px; width: 368px; }
  .chevrons.right { left: 822px; width: 368px; }

  .danger-band { top: 94px; left: 0; width: 1200px; height: 110px; background: var(--yellow); text-align: center; }
  .danger-text { font-weight: 800; font-size: 104px; line-height: 110px; color: var(--black); letter-spacing: 1px; }

  .waste-title { top: 208px; left: 0; width: 1200px; text-align: center; color: var(--yellow); font-weight: 700; font-size: 44px; }

  .no-reuse { left: 30px; top: 288px; width: 72px; height: 72px; }
  .hazard-diamond { left: 34px; top: 290px; width: 336px; height: 336px; }
  .un-number { left: 0; top: 630px; width: 384px; text-align: center; color: var(--white); font-weight: 700; font-size: 52px; line-height: 64px; }
  .un-code { left: 0; top: 697px; width: 386px; text-align: center; color: var(--white); font-weight: 700; font-size: 21px; letter-spacing: 0.4px; }

  .spec { left: 412px; }
  .spec-tag { display: inline-block; background: var(--navy); color: var(--white); font-weight: 700; font-size: 21px; padding: 4px 8px; letter-spacing: 1.3px; }
  .spec-value { color: var(--white); font-weight: 700; font-size: 20px; letter-spacing: 1.6px; margin-top: 10px; padding-left: 8px; }

  .illustration-area { background: var(--white); }

  .navy-base { left: 0; top: 744px; width: 1200px; height: 394px; }
  .warnings { top: 769px; left: 0; width: 1200px; display: flex; justify-content: center; align-items: center; gap: 46px; color: var(--white); font-weight: 700; font-size: 21px; letter-spacing: 1.6px; }
  .warnings .dot { width: 13px; height: 13px; border-radius: 50%; background: var(--white); }

  .info-panel { left: 12px; top: 834px; width: 1176px; height: 288px; background: var(--white); border-radius: 6px; }
  .record-box { left: 34px; top: 854px; width: 705px; height: 250px; background: var(--yellow); border: 2px solid var(--navy); border-radius: 16px; }
  .record-row { position: absolute; left: 16px; width: 670px; height: 52px; display: flex; align-items: center; }
  .record-label { width: 180px; color: var(--navy); font-weight: 700; font-size: 21px; }
  .record-icon { width: 44px; height: 44px; }
  .record-field { margin-left: 18px; width: 423px; height: 52px; background: var(--white); }

  .brand { left: 822px; top: 866px; display: flex; align-items: center; gap: 12px; }
  .brand-mark { width: 28px; height: 28px; background: var(--yellow); }
  .brand-name { color: var(--navy); font-weight: 700; font-size: 52px; line-height: 60px; }
  .maker-city { left: 822px; top: 930px; color: var(--grey); font-size: 27px; }
  .maker-web { left: 822px; top: 964px; color: var(--black); font-weight: 700; font-size: 27px; letter-spacing: 0.5px; }
  .maker-ref { left: 822px; top: 1000px; color: var(--black); font-size: 24px; }
  .maker-ref span { font-size: 22px; margin-left: 10px; }
  .factory { left: 840px; top: 1040px; width: 72px; height: 56px; }
</style>
</head>
<body>
<main class="label">

  <header class="fill-level abs">
    <svg class="chevrons left abs" viewBox="0 0 368 26" aria-hidden="true">
      <defs>
        <pattern id="chev-left" width="26.3" height="26" patternUnits="userSpaceOnUse">
          <polygon points="14,2 21,2 12,13 21,24 14,24 5,13" fill="#fff"/>
        </pattern>
        <pattern id="chev-right" width="26.3" height="26" patternUnits="userSpaceOnUse">
          <polygon points="12,2 5,2 14,13 5,24 12,24 21,13" fill="#fff"/>
        </pattern>
      </defs>
      <rect width="368" height="26" fill="url(#chev-left)"/>
    </svg>
    <div class="fill-level-text abs">FILLING LEVEL</div>
    <svg class="chevrons right abs" viewBox="0 0 368 26" aria-hidden="true">
      <rect width="368" height="26" fill="url(#chev-right)"/>
    </svg>
  </header>

  <section class="danger-band abs"><h1 class="danger-text">DANGER</h1></section>

  <h2 class="waste-title abs">CLINICAL WASTE, Unspecified, N.O.S.”</h2>

  <svg class="no-reuse abs" viewBox="0 0 72 72" role="img" aria-label="Do not reuse">
    <circle cx="36" cy="36" r="32" fill="none" stroke="#fff" stroke-width="4"/>
    <text x="36" y="49" text-anchor="middle" fill="#fff" font-family="Open Sans, sans-serif" font-weight="800" font-size="36">2</text>
    <line x1="14" y1="58" x2="58" y2="14" stroke="#fff" stroke-width="4"/>
  </svg>

  <svg class="hazard-diamond abs" viewBox="0 0 336 336" role="img" aria-label="Class 6 infectious substance hazard label">
    <polygon points="168,2 334,168 168,334 2,168" fill="#fff"/>
    <polygon points="168,16 320,168 168,320 16,168" fill="#000"/>
    <polygon points="168,24 312,168 168,312 24,168" fill="#fff"/>
    <g transform="translate(168,106) scale(1.3)">
      <circle cx="0" cy="-18" r="22" fill="#000"/>
      <circle cx="15.6" cy="9" r="22" fill="#000"/>
      <circle cx="-15.6" cy="9" r="22" fill="#000"/>
      <circle cx="0" cy="-26" r="16" fill="#fff"/>
      <circle cx="22.5" cy="13" r="16" fill="#fff"/>
      <circle cx="-22.5" cy="13" r="16" fill="#fff"/>
      <circle cx="0" cy="0" r="20" fill="none" stroke="#000" stroke-width="5"/>
      <circle cx="0" cy="0" r="7" fill="#fff"/>
      <line x1="0" y1="-7" x2="0" y2="-20" stroke="#fff" stroke-width="3"/>
      <line x1="6" y1="3.5" x2="17.3" y2="10" stroke="#fff" stroke-width="3"/>
      <line x1="-6" y1="3.5" x2="-17.3" y2="10" stroke="#fff" stroke-width="3"/>
    </g>
    <text x="168" y="286" text-anchor="middle" fill="#000" font-family="Open Sans, sans-serif" font-size="28">6</text>
  </svg>

  <div class="un-number abs">UN 3291</div>
  <div class="un-code abs">1H2/Y0,3/S/YR/N/KVP4817B</div>

  <dl class="spec abs" style="top:310px"><dt class="spec-tag">SERIES</dt><dd class="spec-value">NOVA</dd></dl>
  <dl class="spec abs" style="top:420px"><dt class="spec-tag">CERTIFICATION</dt><dd class="spec-value">ISO23907:2012</dd></dl>
  <dl class="spec abs" style="top:523px"><dt class="spec-tag">SIZE</dt><dd class="spec-value">2 2 L</dd></dl>
  <dl class="spec abs" style="top:622px"><dt class="spec-tag">USEFUL CAPACITY</dt><dd class="spec-value">1,76 L</dd></dl>

  <div class="illustration-area abs" style="left:674px;top:284px;width:220px;height:208px" role="img" aria-label="Illustration area"></div>
  <div class="illustration-area abs" style="left:672px;top:514px;width:220px;height:206px" role="img" aria-label="Illustration area"></div>
  <div class="illustration-area abs" style="left:910px;top:284px;width:271px;height:436px" role="img" aria-label="Illustration area"></div>

  <svg class="navy-base abs" viewBox="0 0 1200 394" aria-hidden="true">
    <polygon points="46,0 1154,0 1182,34 1200,34 1200,394 0,394 0,34 24,34" fill="#2a2b62"/>
  </svg>
  <div class="warnings abs">
    <span>AUTOCLAVABLE AT 134 C</span><span class="dot"></span>
    <span>DO NOT FORCE CLOSURE</span><span class="dot"></span>
    <span>DO NOT OVERFILL</span>
  </div>

  <section class="info-panel abs"></section>

  <section class="record-box abs">
    <div class="record-row" style="top:25px">
      <span class="record-label">PLACE/CLINIC</span>
      <svg class="record-icon" viewBox="0 0 44 44" aria-hidden="true">
        <polygon points="22,3 42,17 38,17 38,41 6,41 6,17 2,17" fill="#2a2b62"/>
        <rect x="18" y="19" width="8" height="18" fill="#f2eb1f"/>
        <rect x="13" y="24" width="18" height="8" fill="#f2eb1f"/>
      </svg>
      <span class="record-field"></span>
    </div>
    <div class="record-row" style="top:93px">
      <span class="record-label">DEPARTMENT</span>
      <svg class="record-icon" viewBox="0 0 44 44" aria-hidden="true">
        <rect x="16" y="3" width="12" height="10" fill="#2a2b62"/>
        <path d="M22 13v8M8 21h28M8 21v9M36 21v9M22 21v9" stroke="#2a2b62" stroke-width="3" fill="none"/>
        <rect x="3" y="30" width="10" height="10" fill="#2a2b62"/>
        <rect x="17" y="30" width="10" height="10" fill="#2a2b62"/>
        <rect x="31" y="30" width="10" height="10" fill="#2a2b62"/>
      </svg>
      <span class="record-field"></span>
    </div>
    <div class="record-row" style="top:165px">
      <span class="record-label">SEALING DATE</span>
      <svg class="record-icon" viewBox="0 0 44 44" aria-hidden="true">
        <rect x="5" y="7" width="34" height="33" rx="3" fill="#2a2b62"/>
        <rect x="12" y="3" width="4" height="8" fill="#2a2b62"/>
        <rect x="28" y="3" width="4" height="8" fill="#2a2b62"/>
        <g fill="#f2eb1f">
          <rect x="10" y="18" width="6" height="5"/><rect x="19" y="18" width="6" height="5"/><rect x="28" y="18" width="6" height="5"/>
          <rect x="10" y="27" width="6" height="5"/><rect x="19" y="27" width="6" height="5"/><rect x="28" y="27" width="6" height="5"/>
        </g>
      </svg>
      <span class="record-field"></span>
    </div>
  </section>

  <div class="brand abs"><span class="brand-mark"></span><span class="brand-name">Tidlock</span></div>
  <div class="maker-city abs">Lindholm, Sweden</div>
  <div class="maker-web abs">www.tidlock.eu</div>
  <div class="maker-ref abs">Ref:<span>xxxxx-xx-xx-xx</span></div>
  <svg class="factory abs" viewBox="0 0 72 56" role="img" aria-label="Manufacturer">
    <polygon points="0,56 0,24 16,14 16,24 32,14 32,24 48,14 48,0 58,0 58,14 58,24 72,24 72,56" fill="#000"/>
  </svg>

</main>
</body>
</html>
```